Product Introduction Brochure

Brochure to introduce our mid/high end lighting products to potential wholesalers / Disrtibutors / Retailers. To be mainly graphical but will contain some text also. The purpose of the brochure will be to get potential customers to find out more either by calling us or to visit our website. The brochure should be of A3 size folded in half to an A4. Front page should be mainly logo and name, inner 2 pages should showcase some of the products we can supply together with some text (to be supplied, please use filler text in the initial design), then the back page containing our contact details. The products are lights, floor lamps and table lamps. I have attached a number of images, as well as our company logo. I would prefer the design to be on a black background, however this is not critical
Target Market(s)
Retailer, distribution and wholesale buyers
Interior design consultants and specifiers
Industry/Entity Type
Product
Look and feel
Each slider illustrates characteristics of the customer's brand and the style your logo design should communicate.

```html
<!DOCTYPE html>
<html lang="en">
<head>
<meta charset="utf-8">
<title>Glowen – Product Brochure Spread</title>
<link rel="stylesheet" href="https://fonts.googleapis.com/css2?family=Barlow:wght@400;500;600&family=Questrial&display=swap">
<style>
  :root {
    --ink: #000000;
    --green: #2bb24c;
    --green-bright: #19c75a;
    --green-deep: #0b6b2e;
    --fold: #5a5a5a;
    --text-dark: #111111;
    --text-mid: #2b2b2b;
  }
  * { box-sizing: border-box; margin: 0; padding: 0; }
  html, body { width: 1200px; height: 873px; overflow: hidden; background: #d9d9d9; }
  .spread { position: relative; width: 1200px; height: 873px; display: flex; }
  .page { position: relative; width: 600px; height: 873px; background: var(--ink); overflow: hidden; }
  .page--back { border-right: 1px solid var(--fold); }

  .brand { position: absolute; display: flex; align-items: center; font-family: "Barlow", sans-serif; font-weight: 600; color: var(--green); letter-spacing: -0.5px; white-space: nowrap; z-index: 2; }
  .brand__dot { border-radius: 50%; background: var(--green); flex: none; }

  /* back page */
  .back-brand { left: 228px; top: 282px; gap: 8px; font-size: 31px; }
  .back-brand .brand__dot { width: 48px; height: 48px; }
  .back-glow {
    position: absolute; left: 177px; top: 320px; width: 248px; height: 308px;
    background:
      radial-gradient(ellipse 48% 14% at 50% 36%, rgba(255,255,255,0.95), rgba(255,255,255,0) 100%),
      repeating-linear-gradient(90deg, rgba(0,0,0,0.25) 0 2px, rgba(0,0,0,0) 2px 5px, rgba(0,0,0,0.12) 5px 7px, rgba(0,0,0,0) 7px 11px),
      radial-gradient(ellipse 50% 55% at 50% 42%, var(--green-bright) 0%, #0c8a3a 55%, rgba(0,0,0,0) 100%);
    -webkit-mask-image: linear-gradient(180deg, rgba(0,0,0,0.3), #000 25%, #000 70%, rgba(0,0,0,0));
            mask-image: linear-gradient(180deg, rgba(0,0,0,0.3), #000 25%, #000 70%, rgba(0,0,0,0));
  }
  .contact { position: absolute; left: 246px; top: 400px; font-family: "Questrial", sans-serif; color: var(--text-mid); font-size: 10px; line-height: 12px; list-style: none; white-space: nowrap; z-index: 2; }
  .contact li { display: flex; gap: 5px; align-items: flex-start; }
  .contact svg { width: 8px; height: 10px; flex: none; margin-top: 1px; }
  .contact .contact__address { margin-bottom: 8px; }
  .contact .contact__phone { font-family: "Barlow", sans-serif; font-weight: 600; font-size: 12px; line-height: 14px; color: var(--text-dark); margin-bottom: 8px; }
  .contact .contact__phone svg { margin-top: 2px; }
  .contact .contact__mail { margin-bottom: 3px; }
  .tagline { position: absolute; left: 0; width: 600px; top: 636px; text-align: center; font-family: "Barlow", sans-serif; font-weight: 500; color: var(--green); font-size: 19.5px; line-height: 25px; letter-spacing: 0.3px; }

  /* front page */
  .front-brand { left: 160px; top: 93px; gap: 14px; font-size: 63px; }
  .front-brand .brand__dot { width: 92px; height: 92px; }
  .front-glow {
    position: absolute; left: 0; top: 245px; width: 600px; height: 490px;
    background:
      radial-gradient(ellipse 30% 26% at 64% 52%, rgba(255,255,255,0.9), rgba(255,255,255,0) 100%),
      repeating-linear-gradient(180deg, rgba(0,0,0,0.2) 0 2px, rgba(0,0,0,0) 2px 6px, rgba(0,0,0,0.1) 6px 8px, rgba(0,0,0,0) 8px 13px),
      radial-gradient(ellipse 62% 42% at 62% 50%, var(--green-bright) 0%, #0a9a3f 50%, rgba(0,0,0,0) 100%);
    -webkit-mask-image: linear-gradient(90deg, rgba(0,0,0,0.1), #000 30%, #000 100%);
            mask-image: linear-gradient(90deg, rgba(0,0,0,0.1), #000 30%, #000 100%);
  }
  .headline { position: absolute; left: 225px; width: 320px; top: 337px; text-align: center; font-family: "Questrial", sans-serif; font-weight: 400; color: var(--text-dark); font-size: 39px; line-height: 47px; letter-spacing: -0.5px; white-space: nowrap; z-index: 2; }
  .products { position: absolute; left: 233px; top: 494px; display: flex; gap: 9px; z-index: 2; }
  .product-shot { width: 93px; height: 147px; border-radius: 50%; background: radial-gradient(ellipse at 50% 45%, #4a5a50 0%, #141a16 55%, #000 100%); }
</style>
</head>
<body>
<main class="spread">
  <section class="page page--back">
    <div class="brand back-brand"><span class="brand__dot"></span><span>Glowen</span></div>
    <div class="back-glow"></div>
    <ul class="contact">
      <li class="contact__address">
        <svg viewBox="0 0 8 10"><path d="M4 0a3 3 0 0 0-3 3c0 2.3 3 7 3 7s3-4.7 3-7a3 3 0 0 0-3-3zm0 4.2A1.2 1.2 0 1 1 4 1.8a1.2 1.2 0 0 1 0 2.4z" fill="#111"/></svg>
        <span>XXXXX XXXXX XXXXX<br>XXXXX XXXXX XXXXX</span>
      </li>
      <li class="contact__phone">
        <svg viewBox="0 0 10 10"><path d="M2.2 0.6l1.4 1.9-0.8 1.1c0.5 1.2 1.4 2.1 2.6 2.6l1.1-0.8 1.9 1.4-0.9 1.8C4.2 8.4 0.8 5 0.4 1.5z" fill="none" stroke="#111" stroke-width="0.9"/></svg>
        <span>000-123-4567</span>
      </li>
      <li class="contact__mail">
        <svg viewBox="0 0 10 10"><rect x="0.5" y="2.5" width="9" height="6" fill="#222"/><path d="M0.5 2.5l4.5 3.5 4.5-3.5" fill="none" stroke="#bbb" stroke-width="0.7"/></svg>
        <span>info@glowen.com</span>
      </li>
      <li class="contact__web">
        <svg viewBox="0 0 10 10"><circle cx="5" cy="5" r="4" fill="none" stroke="#222" stroke-width="0.9"/><path d="M1 5h8M5 1c-2 2.5-2 5.5 0 8M5 1c2 2.5 2 5.5 0 8" fill="none" stroke="#222" stroke-width="0.7"/></svg>
        <span>www.glowen.com</span>
      </li>
    </ul>
    <p class="tagline">Our products are<br>lights, Floor lamps and Table lamps</p>
  </section>

  <section class="page page--front">
    <div class="brand front-brand"><span class="brand__dot"></span><span>Glowen</span></div>
    <div class="front-glow"></div>
    <h1 class="headline">BRING<br>BRIGHT LIGHT<br>TO YOUR LIFE</h1>
    <div class="products">
      <div class="product-shot" role="img" aria-label="Photo of a white table lamp with faceted shade"></div>
      <div class="product-shot" role="img" aria-label="Photo of a white pendant light with ribbed round shade"></div>
      <div class="product-shot" role="img" aria-label="Photo of a floor lamp with hanging oval shade"></div>
    </div>
  </section>
</main>
</body>
</html>
```